Romantic Comedy Film Needs a Cool Poster

Need a professional looking poster for our film called Mabel Sunstruck. The film is a romantic comedy about a guy who makes himself allergic to his girlfriend. I'm not sure quite what I want the poster to look like but I've included a few images of Mabel (the main character) so do what you think would look best, even cutting the backgrounds out is encouraged if you have a good vision. It just has to say "Mabel Sunstruck", and that can be in all caps or whatever you think looks best. I'm even open to not using any of the pictures if you can come up with a design that looks good. Note: I probably don't want to use the words "bang bang" in the poster as it will be too distracting, but if you think it would work go for it.
The film is black and white, so keep this in mind when making your poster design. The main inspiration for the film is another film called 'Odile Brun'
The final poster file has to follow standard poster print spec and resolution requirements as we will be printing it large as well submitting the file to film festivals. If the images I've provided are too small to achieve this, just make them a little bigger, I don't mind too much if it looks good.
Any questions, just let me know. Thank you for your time! :)
Industry/Entity Type
Film Production
Font styles to use
Other font styles liked:
- No preference. Probably sans serif, but looking at the poster for the film Odile Brun, Serif seems to work. Go with your judgement.
Colors
Designer to choose colors to be used in the design.
Requirements
Must have
- Must have the title Mabel Sunstruck on the poster without any line break between the words "sun" and "struck". Any capitalisation and font, but the only variation we don't want is "Mabel SunStruck" because "Sunstruck" needs to be conveyed as one word.
Nice to have
- The actual film is entirely black and white, so keep this in mind with your designs. You might want to keep the poster entirely black and white, or even just duller colours. What could maybe work best is just one single colour in addition to the black and white. Search up the Odile Brun poster to see an example of the one extra colour standing out. But I'm not against any colours or ideas.
- The tagline for the film is: His mind is telling him yes, but his body is telling him no.
- Only include this if you think it works well.
Should not have
- There must not be a line break between "sun" and "struck".

```html
<!DOCTYPE html>
<html lang="en">
<head>
<meta charset="utf-8">
<title>Mabel Sunstruck — Film Poster</title>
<link href="https://fonts.googleapis.com/css2?family=Raleway:ital,wght@0,200;1,300&family=Oswald:wght@400;500&display=swap" rel="stylesheet">
<style>
  :root {
    --ink: #07060c;
    --night: #1b1a2b;
    --dusk: #2e2c45;
    --haze: #4a4763;
    --title-red: #a3273c;
    --pale: #cfc8cc;
    --credit: #d9d4d8;
  }
  html, body {
    margin: 0;
    padding: 0;
    overflow: hidden;
    background: var(--ink);
  }
  .poster {
    position: relative;
    width: 900px;
    height: 1200px;
    overflow: hidden;
    background: var(--ink);
  }
  .scene-photo {
    position: absolute;
    inset: 0;
    background:
      radial-gradient(ellipse 70% 55% at 50% 48%, var(--haze) 0%, var(--dusk) 40%, var(--night) 70%, var(--ink) 100%),
      var(--night);
  }
  .credits-shade {
    position: absolute;
    left: 0; right: 0; bottom: 0;
    height: 260px;
    background: linear-gradient(to bottom, rgba(7,6,12,0) 0%, rgba(7,6,12,0.85) 45%, var(--ink) 100%);
  }
  .title {
    position: absolute;
    inset: 0;
  }
  .title-first {
    font-family: "Raleway", sans-serif;
    font-style: italic;
    font-weight: 300;
    font-size: 92px;
    letter-spacing: 6px;
    fill: var(--pale);
  }
  .title-last {
    font-family: "Raleway", sans-serif;
    font-weight: 200;
    font-size: 170px;
    fill: var(--title-red);
    opacity: 0.92;
  }
  .credits {
    position: absolute;
    left: 0; right: 0;
    top: 1040px;
    font-family: "Oswald", sans-serif;
    color: var(--credit);
  }
  .credit-row {
    display: flex;
    justify-content: center;
    align-items: center;
    gap: 12px;
    height: 44px;
    padding-left: 130px;
  }
  .credit {
    display: flex;
    align-items: center;
    gap: 5px;
  }
  .role {
    font-size: 9px;
    line-height: 9px;
    text-transform: uppercase;
    text-align: right;
  }
  .name {
    font-size: 29px;
    font-weight: 400;
    text-transform: uppercase;
    letter-spacing: -1px;
  }
</style>
</head>
<body>
<main class="poster">
  <div class="scene-photo" role="img" aria-label="Black-and-white photo of a young man sitting alone, head in hand, at an empty set dinner table in front of a wall covered with vintage posters"></div>
  <div class="credits-shade"></div>

  <svg class="title" width="900" height="1200" viewBox="0 0 900 1200" aria-label="Mabel Sunstruck">
    <text class="title-first" x="112" y="172">MABEL</text>
    <g class="title-last">
      <text x="130" y="315">S</text>
      <text x="202" y="377">U</text>
      <text x="274" y="439">N</text>
      <text x="346" y="501">S</text>
      <text x="418" y="563">T</text>
      <text x="490" y="625">R</text>
      <text x="562" y="687">U</text>
      <text x="634" y="749">C</text>
      <text x="706" y="811">K</text>
    </g>
  </svg>

  <section class="credits">
    <div class="credit-row">
      <div class="credit"><span class="role">Starring</span><span class="name">Owen Hartley</span></div>
      <div class="credit"><span class="name">Lena Marsh</span></div>
      <div class="credit"><span class="name">Felix Dunmore</span></div>
      <div class="credit"><span class="role">Edited<br>by</span><span class="name">Milo Ferrante</span></div>
    </div>
    <div class="credit-row">
      <div class="credit"><span class="role">Music<br>by</span><span class="name">Wen Li Tan</span></div>
      <div class="credit"><span class="role">Sound<br>designer</span><span class="name">Nathan Pryce</span></div>
      <div class="credit"><span class="role">Production<br>designer</span><span class="name">Clara Benton</span></div>
      <div class="credit"><span class="role">Director of<br>photography</span><span class="name">Iris Wong</span></div>
    </div>
    <div class="credit-row">
      <div class="credit"><span class="role">Produced<br>by</span><span class="name">Daniel Ashcroft</span></div>
      <div class="credit"><span class="name">Ivy Castellane</span></div>
      <div class="credit"><span class="role">Written and<br>directed by</span><span class="name">Owen Hartley</span></div>
    </div>
  </section>
</main>
</body>
</html>
```